Business Card Design

Tumble Bay is a Laundromat Store
we provide wash and Fold service to Customers who are busy with their life and can not come to the store and do laundry
we have customers who drop their laundry at the store
but now i want to provide service to customers who are not able to come to the store to drop. i will go to their address and pickup the laundry and get it washed folded and delivered
Updates
Can you use the colour in you design which i uploaded and also fusha fluorescent green bright pink
Target Market(s)
all works of life who don't have time to do laundry
Industry/Entity Type
Store
Contact Information for Business Card
TumbleBay Laundromat
482 Orchard Lane
Lynn MA 01957
Look and feel
Each slider illustrates characteristics of the customer's brand and the style your logo design should communicate.

```html
<!DOCTYPE html>
<html lang="en">
<head>
<meta charset="utf-8">
<title>TumbleBay Laundromat – Business Card</title>
<link href="https://fonts.googleapis.com/css2?family=Lato:wght@300;400;700;900&display=swap" rel="stylesheet">
<style>
  :root {
    --stage: #2a2a2a;
    --sky: #c7dcf0;
    --sky-deep: #a9c6e6;
    --magenta: #a5237f;
    --plum: #8a2a78;
    --plum-light: #a8459a;
    --royal: #1e5fb0;
    --royal-light: #3a7fc9;
    --ink: #1b1b1b;
    --white: #ffffff;
  }
  * { box-sizing: border-box; margin: 0; padding: 0; }
  html, body {
    width: 1200px; height: 900px; overflow: hidden;
    background: var(--stage);
    font-family: "Lato", Arial, sans-serif;
  }
  .card {
    position: absolute; left: 75px; top: 150px;
    width: 1050px; height: 600px; overflow: hidden;
    background: linear-gradient(180deg, var(--sky) 0%, var(--sky-deep) 100%);
    box-shadow: 0 20px 50px rgba(0,0,0,.5);
  }
  .brand {
    position: absolute; top: 34px; left: 0; width: 100%;
    text-align: center; color: var(--magenta);
    font-size: 50px; line-height: 1;
  }
  .brand-name { font-weight: 700; }
  .brand-type { font-weight: 400; }
  .address {
    position: absolute; top: 98px; left: 0; width: 100%;
    text-align: center; color: var(--ink);
    font-size: 25px; font-weight: 400; letter-spacing: 2.5px;
  }
  .call {
    position: absolute; top: 145px; left: 50%; transform: translateX(-50%);
    background: var(--royal); color: var(--white);
    font-size: 25px; font-weight: 700; letter-spacing: 1px;
    padding: 8px 18px; white-space: nowrap;
  }
  .photo {
    position: absolute; border-radius: 40px;
  }
  .photo-dirty {
    left: 270px; top: 215px; width: 180px; height: 150px;
    background: radial-gradient(circle at 50% 55%, #c7a2b8 0%, #9c6f8f 55%, rgba(156,111,143,0) 75%);
  }
  .photo-clean {
    left: 620px; top: 195px; width: 175px; height: 170px; border-radius: 12px;
    background: linear-gradient(180deg, #b46fb2 0%, #7c8fbf 35%, #d4577d 60%, #4f8c7c 80%, #6a5b8c 100%);
  }
  .transfer { position: absolute; left: 460px; top: 210px; width: 170px; height: 170px; }
  .band { position: absolute; left: 0; top: 330px; width: 1050px; height: 270px; }
  .step {
    position: absolute; top: 370px; width: 110px; height: 110px;
    margin-left: -55px; border-radius: 50%;
    background: var(--white);
    box-shadow: 0 4px 10px rgba(0,0,0,.3);
    display: flex; align-items: center; justify-content: center;
  }
  .step-art { width: 76px; height: 76px; border-radius: 50%; }
  .art-schedule { background: linear-gradient(180deg, #e5e5e5, #9a9a9a); }
  .art-home { background: linear-gradient(180deg, #e98a3c, #3f8fd6); }
  .art-wash { background: linear-gradient(180deg, #8db24a, #5a5a5a); }
  .art-happy { background: radial-gradient(circle, #ffd93b 0%, #f2b400 100%); }
  .caption {
    position: absolute; top: 500px; width: 260px; margin-left: -130px;
    text-align: center; color: var(--white);
    font-size: 20px; font-weight: 700; line-height: 1.25;
  }
  .flow { position: absolute; left: 0; top: 370px; width: 1050px; height: 110px; pointer-events: none; }
</style>
</head>
<body>
  <main class="card">
    <h1 class="brand"><span class="brand-name">TumbleBay</span> <span class="brand-type">LAUNDROMAT</span></h1>
    <p class="address">482 ORCHARD LANE LYNN MA 01957</p>
    <p class="call">CALL US: 079 555 01234</p>

    <div class="photo photo-dirty" role="img" aria-label="Photo of a heap of crumpled dirty laundry"></div>
    <div class="photo photo-clean" role="img" aria-label="Photo of a neat stack of folded clean clothes"></div>

    <svg class="transfer" viewBox="0 0 170 170" aria-label="From dirty to clean">
      <circle cx="85" cy="85" r="78" fill="var(--royal-light)" stroke="#ffffff" stroke-width="4"/>
      <text x="85" y="68" text-anchor="middle" fill="#fff" font-family="Lato, sans-serif" font-size="30" font-weight="400">FROM</text>
      <line x1="28" y1="85" x2="142" y2="85" stroke="#fff" stroke-width="2" stroke-dasharray="5 4"/>
      <path d="M28 85 l10 -6 v12 z" fill="#fff"/>
      <text x="85" y="125" text-anchor="middle" fill="#fff" font-family="Lato, sans-serif" font-size="32" font-weight="900">TO</text>
      <line x1="40" y1="140" x2="140" y2="140" stroke="#fff" stroke-width="2" stroke-dasharray="5 4"/>
      <path d="M142 140 l-10 -6 v12 z" fill="#fff"/>
    </svg>

    <svg class="band" viewBox="0 0 1050 270" preserveAspectRatio="none" aria-hidden="true">
      <defs>
        <linearGradient id="plumFill" x1="0" y1="0" x2="0" y2="1">
          <stop offset="0" stop-color="var(--plum-light)"/>
          <stop offset="1" stop-color="var(--plum)"/>
        </linearGradient>
      </defs>
      <path d="M0 80 Q525 -10 1050 80 L1050 270 L0 270 Z" fill="url(#plumFill)"/>
      <path d="M0 80 Q525 -10 1050 80" fill="none" stroke="#ffffff" stroke-opacity=".6" stroke-width="3"/>
      <rect x="0" y="140" width="1050" height="130" fill="var(--royal)"/>
    </svg>

    <svg class="flow" viewBox="0 0 1050 110" aria-hidden="true">
      <g fill="none" stroke="#fff" stroke-width="2.5" stroke-dasharray="7 5">
        <path d="M225 60 Q300 80 370 58"/>
        <path d="M510 58 Q570 78 625 52"/>
        <path d="M765 52 Q820 70 862 50"/>
      </g>
      <g fill="#fff">
        <path d="M382 54 l-14 -4 l4 12 z"/>
        <path d="M637 48 l-14 -3 l5 12 z"/>
        <path d="M874 46 l-14 -2 l5 12 z"/>
      </g>
    </svg>

    <div class="step" style="left:155px"><div class="step-art art-schedule" role="img" aria-label="Illustration of a schedule calendar"></div></div>
    <div class="step" style="left:440px"><div class="step-art art-home" role="img" aria-label="Illustration of a house"></div></div>
    <div class="step" style="left:695px"><div class="step-art art-wash" role="img" aria-label="Illustration of laundry being washed and delivered"></div></div>
    <div class="step" style="left:925px"><div class="step-art art-happy" role="img" aria-label="Illustration of a happy customer emoticon"></div></div>

    <p class="caption" style="left:155px">You Schedule<br>A Pick-Up</p>
    <p class="caption" style="left:440px">We Pick-Up<br>Your Dirty Laundry</p>
    <p class="caption" style="left:695px">We Wash, Dry, Fold<br>&amp; Return Clean Laundry</p>
    <p class="caption" style="left:925px">Enjoy Effortless<br>Clean Laundry</p>
  </main>
</body>
</html>
```